Tidecrest NZ Brand, Revenue, Promotions & Events

I need an innovative business card that pops my brand. I like the colours against darker gradients and i'm not afraid to be bold.

I run my own Business, Brand, Event & Promotion company. I specialise in breathing life into businesses and adding atmosphere to promotions and events. I am concept based lady that likes to test the boundaries and create stand out campaigns that connect with the consumer.

I have 12 years business experience in a realm of interesting fields form 11 years in coordinating international music festivals & promotions, 6 years in radio with 8 radio awards including a NZ radio award for best sales team in NZ and was the national brand and sales manager for New Zealands 1st indoor entertainment mall. With 10 years of experience in advertising sales, I have an eye for creating revenue streams for businesses and thrive on implementing campaigns that compliment those streams.

I love sayings like "Do what you love, love what you do" and believe that you can achieve anything you want.

I have been fortunate in my career that my connections have carried me without needing to promote my business however it is important that I start to do so.

Target Market(s)

Decision makers 25 to 54

Contact Information for Business Card

Petra Ollingham
Director
p. 022 587 3091
e. petra@tidecrest.nz
www.tidecrest.nz

FB, IG and Linkedin logo

Font styles to use
Sans Serif

Colors

Designer to choose colors to be used in the design.

Requirements
Must have
• Petra Ollingham
• Director
• p. 022 587 3091
• e. petra@tidecrest.nz
• www.tidecrest.nz
• FB, IG and Linkedin logo
Nice to have
• I am looking for a business card with character, that leaves my presence with my customer and makes them remember my brand & optimistic personality when i walk out the door.

```html
<!DOCTYPE html>
<html lang="en">
<head>
<meta charset="utf-8">
<title>Tidecrest NZ — Business Card</title>
<link href="https://fonts.googleapis.com/css2?family=Roboto:wght@300;400;500&display=swap" rel="stylesheet">
<style>
  :root{
    --bg:#e4e4e4;
    --card:#ffffff;
    --blue:#2a9fe0;
    --grey:#9b9b9b;
    --rule:#c9c9c9;
  }
  *{box-sizing:border-box;margin:0;padding:0}
  html,body{width:1200px;height:801px;overflow:hidden}
  body{
    background:var(--bg);
    font-family:"Roboto",Arial,sans-serif;
    display:flex;align-items:center;justify-content:center;gap:40px;
  }
  .card{
    width:540px;height:309px;background:var(--card);
    border-bottom:5px solid var(--blue);
    box-shadow:0 10px 30px rgba(0,0,0,.12);
    position:relative;
  }
  .brand{display:flex;flex-direction:column}
  .brand-name{
    display:flex;align-items:center;gap:8px;
    color:var(--blue);font-weight:500;letter-spacing:.06em;text-transform:uppercase;line-height:1;
    white-space:nowrap;
  }
  .brand-dot{width:.55em;height:.55em;border-radius:50%;background:var(--blue)}
  .brand-tagline{color:var(--grey);text-transform:uppercase;letter-spacing:.04em;line-height:1;margin-top:6px;white-space:nowrap}

  /* contact side */
  .card-contact .brand{position:absolute;left:36px;top:150px}
  .card-contact .brand-name{font-size:26px}
  .card-contact .brand-tagline{font-size:9.5px}
  .divider{position:absolute;left:280px;top:56px;width:1px;height:120px;background:var(--rule)}
  .details{position:absolute;left:304px;top:56px}
  .person-name{color:var(--blue);font-weight:500;font-size:19px}
  .person-role{color:var(--grey);font-weight:300;font-size:14px;margin-top:4px}
  .contact-list{list-style:none;margin-top:14px}
  .contact-list li{display:flex;align-items:center;gap:10px;color:var(--grey);font-weight:300;font-size:14px;margin-bottom:6px}
  .contact-list svg{width:12px;height:12px;flex:none}
  .socials{position:absolute;left:330px;top:240px;display:flex;gap:9px}
  .social{width:20px;height:20px;border-radius:4px;background:var(--blue)}

  /* logo side */
  .card-logo .brand{position:absolute;left:0;right:0;top:118px;align-items:center}
  .card-logo .brand-name{font-size:42px}
  .card-logo .brand-tagline{font-size:15px;margin-top:10px}
</style>
</head>
<body>
  <section class="card card-contact">
    <div class="brand">
      <div class="brand-name"><span class="brand-dot"></span>Tidecrest NZ</div>
      <div class="brand-tagline">Brand | Growth | Events &amp; Campaigns</div>
    </div>
    <div class="divider"></div>
    <div class="details">
      <div class="person-name">Petra Ollingham</div>
      <div class="person-role">Director</div>
      <ul class="contact-list">
        <li><svg viewBox="0 0 12 12"><path d="M2.5 1h2l1 3-1.3 1a6 6 0 0 0 2.8 2.8l1-1.3 3 1v2a1.5 1.5 0 0 1-1.5 1.5A9.5 9.5 0 0 1 1 2.5 1.5 1.5 0 0 1 2.5 1z" fill="var(--blue)"/></svg>022 587 3091</li>
        <li><svg viewBox="0 0 12 12"><rect x=".8" y="2.3" width="10.4" height="7.4" fill="none" stroke="var(--blue)" stroke-width="1.2"/><path d="M1 2.6 6 6.5l5-3.9" fill="none" stroke="var(--blue)" stroke-width="1.2"/></svg>petra@tidecrest.nz</li>
        <li><svg viewBox="0 0 12 12"><circle cx="6" cy="6" r="5" fill="none" stroke="var(--blue)" stroke-width="1.2"/><ellipse cx="6" cy="6" rx="2.2" ry="5" fill="none" stroke="var(--blue)" stroke-width="1"/><path d="M1 6h10" stroke="var(--blue)" stroke-width="1"/></svg>www.tidecrest.nz</li>
      </ul>
    </div>
    <div class="socials">
      <span class="social" role="img" aria-label="Social profile link"></span>
      <span class="social" role="img" aria-label="Social profile link"></span>
      <span class="social" role="img" aria-label="Social profile link"></span>
    </div>
  </section>

  <section class="card card-logo">
    <div class="brand">
      <div class="brand-name"><span class="brand-dot"></span>Tidecrest NZ</div>
      <div class="brand-tagline">Brand | Growth | Events &amp; Campaigns</div>
    </div>
  </section>
</body>
</html>
```